HRC

This is to hand out to folks at conferences to tell them about this list serve and direct them to the site to email in to join it.
This is a networking and resource site for mental health and addiction professionals.
The mission statement on the ABOUT page needs to be on it.
Then the website address and my name Marta Quillon, LICSW
List Serve Moderator and my email Marta@MartaQuillon.net
and my phone 202-555-0148.
Please see website: www.harborreferralcircle.net

Industry/Entity Type

Mental Health

Contact Information for Business Card

Front: name Harbor Referral Circle and mission statement on the "About" page and put website address: www.harborreferralcircle.net and my name Marta Quillon, LICSW ListServ Moderator
Back: info on the list serve with instructions to go to Contact Us page.
Anything you all think might be useful and still look good.
Put my cell # on the back, 202-555-0193

```html
<!DOCTYPE html>
<html lang="en">
<head>
<meta charset="utf-8">
<title>Harbor Referral Circle – Business Card</title>
<link rel="stylesheet" href="https://fonts.googleapis.com/css2?family=Exo:wght@400;500&display=swap">
<style>
  :root {
    --stage: #2b2b2d;
    --brand-blue: #3d3f98;
    --paper-light: #ffffff;
    --paper-mid: #dcdcde;
    --ink-dark: #333338;
    --ink-white: #ffffff;
  }
  * { box-sizing: border-box; margin: 0; padding: 0; }
  html, body {
    width: 1200px; height: 870px; overflow: hidden;
    background: var(--stage);
    font-family: "Exo", sans-serif;
  }
  .stage { position: relative; width: 1200px; height: 870px; }
  .card {
    position: absolute; width: 560px; height: 320px;
    box-shadow: 0 10px 30px rgba(0,0,0,.55);
    overflow: hidden;
  }
  /* back side */
  .card--back { left: 60px; top: 80px; background: var(--brand-blue); }
  .card--back .company-name {
    position: absolute; left: 150px; top: 160px;
    color: var(--ink-white); font-size: 30px; font-weight: 500; letter-spacing: 1px;
  }
  /* front side */
  .card--front { left: 580px; top: 470px; background: var(--brand-blue); }
  .card--front .info-panel {
    position: absolute; left: 0; top: 0; width: 100%; height: 172px;
    background: linear-gradient(160deg, var(--paper-mid) 0%, var(--paper-light) 55%, var(--paper-mid) 100%);
  }
  .contact-list {
    position: absolute; left: 22px; top: 18px; list-style: none;
    color: var(--ink-dark); font-size: 12px; line-height: 21px;
  }
  .contact-list li { display: flex; align-items: center; gap: 8px; }
  .contact-list svg { width: 12px; height: 12px; fill: var(--ink-dark); flex: none; }
  .card--front .company-name {
    position: absolute; right: 26px; top: 70px; text-align: right;
    color: var(--brand-blue); font-size: 26px; font-weight: 500; line-height: 32px; letter-spacing: .5px;
  }
  .mission {
    position: absolute; left: 24px; top: 196px; width: 260px;
    color: var(--ink-white); font-size: 16px; line-height: 22px;
  }
  .person {
    position: absolute; right: 26px; bottom: 26px; text-align: right; color: var(--ink-white);
  }
  .person-name { font-size: 20px; font-weight: 500; letter-spacing: 1px; }
  .person-title { font-size: 15px; letter-spacing: .5px; }
</style>
</head>
<body>
<main class="stage">
  <section class="card card--back">
    <p class="company-name">Harbor Referral Circle</p>
  </section>

  <section class="card card--front">
    <div class="info-panel">
      <ul class="contact-list">
        <li><svg viewBox="0 0 12 12"><path d="M2 1h3l1 3-2 1a7 7 0 0 0 3 3l1-2 3 1v3c-6 1-10-4-9-9z"/></svg>202-555-0148</li>
        <li><svg viewBox="0 0 12 12"><path d="M3 0h6v12H3zM4 1.5v8h4v-8z"/></svg>202-555-0193</li>
        <li><svg viewBox="0 0 12 12"><path d="M0 5h8V2l4 4-4 4V7H0z"/></svg>Join: see Contact Us page</li>
        <li><svg viewBox="0 0 12 12"><path d="M0 2h12v8H0zM1 3l5 4 5-4z"/></svg>Marta@MartaQuillon.net</li>
        <li><svg viewBox="0 0 12 12"><path d="M6 0a6 6 0 1 0 0 12A6 6 0 0 0 6 0zm-1 1.2C4 3 3.7 4.5 3.6 5.5H1.3A5 5 0 0 1 5 1.2zm2 0a5 5 0 0 1 3.7 4.3H8.4C8.3 4.5 8 3 7 1.2zM6 1.5c.9 1.4 1.3 2.8 1.4 4H4.6c.1-1.2.5-2.6 1.4-4zM1.3 6.5h2.3c.1 1 .4 2.5 1.4 4.3a5 5 0 0 1-3.7-4.3zm3.3 0h2.8c-.1 1.2-.5 2.6-1.4 4-.9-1.4-1.3-2.8-1.4-4zm3.8 0h2.3A5 5 0 0 1 7 10.8c1-1.8 1.3-3.3 1.4-4.3z"/></svg>www.harborreferralcircle.net</li>
      </ul>
      <p class="company-name">Harbor Referral<br>Circle</p>
    </div>
    <p class="mission">Resources for mental health<br>&amp; addiction pros</p>
    <div class="person">
      <p class="person-name">MARTA QUILLON, LICSW</p>
      <p class="person-title">List Serve Moderator</p>
    </div>
  </section>
</main>
</body>
</html>
```